Skatepark, and Teenage Music/Recreation Venue needs logo, business card and letterhead. Website desi

- Logo, Letterhead & Business Card design for a new start Skatepark and Youth Venue called "The Orbit" (Pty.Ltd company) in Australia.

- Website and App design will follow within 6-months.

- Facility centered around world class skatepark which incorporates the use of innovative technology applications to enhance consumer experience, it will also provide a live entertainment & music venue for teenagers.

- Appearance should appeal to the 'mature' teenage population, the aim is provide an excellent membership experience which can be associated with the club brand.

Overall the design should communicate:
Excitement, energy, exclusivity and style

- Clean and modern fonts and styling preferred.
- Logos the I personally like: Brinmore, Quellstone, (but they don't have to be round!)
- Generally I prefer understated business cards that are subtlety/elegently distinct
- ideally the logo would be expected to standalone if no text were available. (if that makes sense?)

Business

The Orbit

```html
<!DOCTYPE html>
<html lang="en">
<head>
<meta charset="utf-8">
<title>The Orbit — Identity</title>
<link href="https://fonts.googleapis.com/css2?family=Michroma&family=Open+Sans:wght@300;400;600&display=swap" rel="stylesheet">
<style>
  :root {
    --orange: #ec5a1c;
    --orange-deep: #d94a12;
    --orange-soft: #f28a55;
    --ink: #1d1d1d;
    --grey-text: #555555;
    --paper: #ffffff;
    --backdrop: #f1f1f1;
  }
  * { box-sizing: border-box; margin: 0; padding: 0; }
  html, body {
    width: 1200px; height: 2472px; overflow: hidden;
    background: var(--backdrop);
    font-family: "Open Sans", sans-serif;
    color: var(--ink);
  }
  .canvas { position: relative; width: 1200px; height: 2472px; }

  .wordmark {
    font-family: "Michroma", sans-serif;
    letter-spacing: 0.04em;
    white-space: nowrap;
    display: flex; align-items: center;
  }
  .wordmark .dot { border-radius: 50%; background: var(--orange); flex: none; }

  /* Primary logo */
  .brand-lockup {
    position: absolute; top: 210px; left: 0; width: 1200px;
    display: flex; justify-content: center;
  }
  .brand-lockup .wordmark { font-size: 56px; color: var(--ink); gap: 26px; }
  .brand-lockup .dot { width: 64px; height: 64px; }

  /* Business cards */
  .card {
    position: absolute; top: 640px; width: 380px; height: 640px;
    box-shadow: 0 10px 24px rgba(0,0,0,0.12);
  }
  .card--front { left: 170px; background: var(--orange); }
  .card--back { left: 650px; background: var(--paper); }

  .card--front .wordmark {
    position: absolute; top: 220px; left: 0; width: 100%;
    justify-content: center; color: var(--paper); font-size: 30px; gap: 14px;
  }
  .card--front .dot { width: 34px; height: 34px; background: var(--paper); }
  .card--front .web {
    position: absolute; bottom: 70px; left: 0; width: 100%; text-align: center;
    font-family: "Michroma", sans-serif; font-size: 17px; letter-spacing: 0.12em;
    color: var(--ink);
  }

  .card--back .wordmark {
    position: absolute; top: 110px; left: 0; width: 100%;
    justify-content: center; font-size: 26px; gap: 12px; color: var(--ink);
  }
  .card--back .dot { width: 28px; height: 28px; }
  .card--back .holder {
    position: absolute; top: 300px; left: 0; width: 100%; text-align: center;
  }
  .holder .name { font-size: 26px; font-weight: 300; color: var(--grey-text); }
  .holder .role { font-size: 14px; font-weight: 400; color: var(--grey-text); margin-top: 4px; }
  .card--back .contact {
    position: absolute; top: 430px; left: 0; width: 100%; text-align: center;
    font-size: 17px; font-weight: 300; line-height: 1.7; color: var(--grey-text);
  }

  /* Letterhead */
  .letterhead {
    position: absolute; top: 1400px; left: 250px; width: 700px; height: 990px;
    background: var(--paper);
    box-shadow: 0 10px 28px rgba(0,0,0,0.14);
  }
  .letterhead .side-band {
    position: absolute; top: 0; left: 0; width: 128px; height: 100%;
    background: linear-gradient(180deg, var(--orange) 0%, var(--orange-deep) 55%, var(--orange-soft) 100%);
  }
  .letterhead .wordmark {
    position: absolute; top: 90px; left: 190px;
    font-size: 22px; gap: 10px; color: var(--ink);
  }
  .letterhead .dot { width: 24px; height: 24px; }
  .letterhead .sender {
    position: absolute; top: 78px; right: 40px; text-align: right;
    font-size: 11px; line-height: 1.55; color: var(--orange);
  }
  .letterhead .body {
    position: absolute; top: 190px; left: 190px; width: 460px;
    font-size: 11.5px; line-height: 1.6; color: var(--grey-text);
  }
  .letterhead .body p { margin-bottom: 16px; }
  .letterhead .signature {
    position: absolute; top: 760px; left: 300px; width: 110px; height: 44px;
    background: linear-gradient(90deg, #e3e3e3, #cfcfcf);
    border-radius: 4px;
  }
  .letterhead .sign-off {
    position: absolute; top: 812px; left: 300px;
    font-size: 11px; line-height: 1.4; color: var(--ink); font-weight: 600;
  }
</style>
</head>
<body>
<main class="canvas">

  <header class="brand-lockup">
    <div class="wordmark"><span class="dot"></span>THE ORBIT</div>
  </header>

  <section class="card card--front">
    <div class="wordmark"><span class="dot"></span>THE ORBIT</div>
    <div class="web">WWW.THEORBIT.COM</div>
  </section>

  <section class="card card--back">
    <div class="wordmark"><span class="dot"></span>THE ORBIT</div>
    <div class="holder">
      <div class="name">Sam Reyes</div>
      <div class="role">President</div>
    </div>
    <div class="contact">
      <div>555.010.0199</div>
      <div>sam.reyes@theorbit.com</div>
    </div>
  </section>

  <article class="letterhead">
    <div class="side-band" role="img" aria-label="Orange band with faded skater and guitarist silhouettes and pixel equaliser blocks"></div>
    <div class="wordmark"><span class="dot"></span>THE ORBIT</div>
    <address class="sender" style="font-style: normal;">
      Consectetur adipiscing elit.<br>
      Sed gravida viverra 435<br>
      5550147820
    </address>
    <div class="body">
      <p>Lorem ipsum dolor sit amet.</p>
      <p>Consectetur adipiscing elit. Sed gravida viverra neque at iaculis. Nulla placerat nunc ut leo lobortis, sed rutrum sem ultrices. Etiam a pharetra tortor. Curabitur feugiat dui et facilisis facilisis. Etiam mollis consequat iaculis. Ut lobortis sit amet mi volutpat. Integer venenatis tempus sem, in porttitor lorem hendrerit ut. Cras pharetra ornare odio sed viverra. Sed sit amet gravida sit amet sapien quis imperdiet aliquam nibh.</p>
      <p>Mauris posuere vehicula nisl viverra iaculis. Lorem ipsum dolor sit amet, consectetur adipiscing elit. Duis tempus blandit turpis, et porta quam suscipit sit amet. Morbi ullamcorper vestibulum mi. Donec nec pellentesque egestas hendrerit vel vestibulum in dui. Vestibulum molestie sit amet velit consequat molestie. Duis aliquam nisl eget nulla dictum scelerisque. Cras sagittis fringilla leo vitae fringilla.</p>
      <p>Suspendisse rhoncus mattis porttitor ac augue. Quisque eget euismod purus. Vestibulum pharetra posuere urna. Nam fringilla neque eu semper laoreet. Praesent nulla diam, interdum a maximus vel, maximus vitae erat. Phasellus gravida nunc et elit porta.</p>
    </div>
    <div class="signature" role="img" aria-label="Handwritten signature"></div>
    <div class="sign-off">Lorem ipsum<br>dolor sit amet</div>
  </article>

</main>
</body>
</html>
```